selling natural honey, a sticker showing scenery and creating interest for consumers

i need a design that portrays a natural product and has an energetic feel about it. the product is natural honey from the country. The honey is sourced from the South Burnett region of Queensland and will be sold to stores. The company selling the product is Marrowick Provisions. The sticker needs to be energetic and also interesting with a level of sophistication.

25-50 mainly females who enjoy natural prducts and willing to pay for good qaulity

It Company

• a nice scenery background, like hills or open paddocks to portray a country/ natural product.

must have 'Marrowick Provisions'

and

'Tarrowin Vale Honey'

included on the sticker
• scenery, maybe a bee or two flying around.
• can't have too much of a cartoon look.

needs to be relatively simple and elegant

```html
<!DOCTYPE html>
<html lang="en">
<head>
<meta charset="utf-8">
<title>Tarrowin Vale Honey – Sticker</title>
<link href="https://fonts.googleapis.com/css2?family=Open+Sans:wght@400;600&family=Righteous&display=swap" rel="stylesheet">
<style>
  :root {
    --page-bg: #f7f7f7;
    --sticker-edge: #e9ebe4;
    --grass-deep: #24561a;
    --grass-mid: #4f8f26;
    --grass-bright: #9ccc3c;
    --grass-light: #b9dd55;
    --cream: #f6f3d8;
    --bee-amber: #c98a1e;
    --bee-dark: #5a3a10;
  }
  html, body {
    margin: 0;
    width: 1200px;
    height: 848px;
    overflow: hidden;
    background: var(--page-bg);
  }
  .canvas {
    position: relative;
    width: 1200px;
    height: 848px;
  }
  .sticker {
    position: absolute;
    left: 360px;
    top: 184px;
    width: 480px;
    height: 480px;
    filter: drop-shadow(0 1px 2px rgba(0,0,0,0.12));
  }
  .sticker__origin {
    font-family: "Open Sans", sans-serif;
    font-weight: 600;
    font-size: 19.5px;
    fill: var(--cream);
  }
  .sticker__product {
    font-family: "Righteous", sans-serif;
    font-size: 50px;
    fill: var(--cream);
    letter-spacing: 1px;
  }
  .sticker__maker {
    font-family: "Open Sans", sans-serif;
    font-weight: 400;
    font-size: 14px;
    fill: var(--cream);
  }
</style>
</head>
<body>
<main class="canvas">
  <svg class="sticker" viewBox="0 0 282 282" xmlns="http://www.w3.org/2000/svg">
    <defs>
      <clipPath id="sticker-shape">
        <circle cx="141" cy="141" r="139"/>
      </clipPath>
      <linearGradient id="hills-tone" x1="0" y1="0" x2="0.25" y2="1">
        <stop offset="0" stop-color="var(--grass-deep)"/>
        <stop offset="0.22" stop-color="var(--grass-mid)"/>
        <stop offset="0.38" stop-color="var(--grass-bright)"/>
        <stop offset="0.55" stop-color="var(--grass-mid)"/>
        <stop offset="0.72" stop-color="var(--grass-light)"/>
        <stop offset="1" stop-color="var(--grass-mid)"/>
      </linearGradient>
      <radialGradient id="bee-tone" cx="0.5" cy="0.5" r="0.5">
        <stop offset="0" stop-color="var(--bee-amber)"/>
        <stop offset="1" stop-color="var(--bee-dark)"/>
      </radialGradient>
    </defs>

    <circle class="sticker__edge" cx="141" cy="141" r="141" fill="var(--sticker-edge)"/>
    <g clip-path="url(#sticker-shape)">
      <rect class="sticker__scenery" x="0" y="0" width="282" height="282" fill="url(#hills-tone)"
            role="img" aria-label="Photograph of rolling green grassy hills under soft light"/>
    </g>

    <text class="sticker__origin" x="21" y="109">TARROWIN VALE</text>
    <text class="sticker__product" x="19" y="158">HONEY</text>
    <text class="sticker__maker" x="118" y="180">marrowick provisions</text>

    <ellipse class="sticker__bee" cx="252" cy="133" rx="22" ry="26" fill="url(#bee-tone)" opacity="0.85"
             role="img" aria-label="Realistic honey bee in flight beside the word Honey"/>
  </svg>
</main>
</body>
</html>
```